Brightwell Consulting Business Card Design

Business Card Design for Brightwell Consulting. Brightwell Consulting is a boutique consultancy based in Atlanta, GA., that specializes in marketing strategy, organization planning, and leadership development. We provide solutions for small businesses and startups as well as Summit 400 companies.

http://brightwellconsulting.example/

Target Market(s)

We provide solutions for small businesses and startups as well as Summit 400 companies.

Industry/Entity Type

Consulting

Contact Information for Business Card

Two sided business card with priority on contact information, logo, tag line (Guidance to Plan Bigger, Act Sooner, Grow Further)

Colors

Designer to choose colors to be used in the design.

Requirements
Must have
• contact information, logo, tag line (Guidance to Plan Bigger, Act Sooner, Grow Further)
• Simple no over communication.
Nice to have
• I would like to see different placements of logo and creative use of both sides of the card
Should not have
• Do not put too much information on the card.

```html
<!DOCTYPE html>
<html lang="en">
<head>
<meta charset="utf-8">
<title>Brightwell Consulting Business Card</title>
<link rel="stylesheet" href="https://fonts.googleapis.com/css2?family=Montserrat:wght@400;600&display=swap">
<style>
  :root {
    --backdrop: #4a4a4a;
    --card: #333333;
    --ink-light: #f2f2f2;
    --front-mark: #8c8c8c;
  }
  * { margin: 0; padding: 0; box-sizing: border-box; }
  html, body { width: 799px; height: 1200px; overflow: hidden; }
  body {
    background: var(--backdrop);
    font-family: "Montserrat", sans-serif;
    position: relative;
  }
  .card {
    position: absolute;
    left: 80px;
    width: 640px;
    height: 366px;
    background: var(--card);
    border-radius: 30px;
    overflow: hidden;
  }
  .card--front { top: 150px; }
  .card--back { top: 684px; }

  .brand {
    position: absolute;
    display: flex;
    align-items: center;
    gap: 14px;
    font-weight: 600;
    white-space: nowrap;
  }
  .brand__square { display: block; border-radius: 3px; }
  .card--front .brand {
    left: 50%;
    top: 50%;
    transform: translate(-50%, -50%);
    font-size: 42px;
    color: var(--front-mark);
  }
  .card--front .brand__square { width: 30px; height: 30px; background: var(--front-mark); }
  .card--back .brand {
    left: 36px;
    top: 92px;
    font-size: 26px;
    color: var(--ink-light);
  }
  .card--back .brand__square { width: 20px; height: 20px; background: var(--ink-light); }

  .contact {
    position: absolute;
    left: 360px;
    top: 150px;
    color: var(--ink-light);
  }
  .contact__name { font-size: 22px; font-weight: 600; margin-bottom: 12px; }
  .contact__line { font-size: 14px; font-weight: 400; line-height: 1.45; white-space: nowrap; }
  .tagline {
    position: absolute;
    left: 36px;
    bottom: 40px;
    font-size: 16px;
    font-weight: 400;
    color: var(--ink-light);
    letter-spacing: 0.3px;
    white-space: nowrap;
  }
</style>
</head>
<body>
  <section class="card card--front" aria-label="Card front">
    <div class="brand">
      <span class="brand__square"></span>
      <span class="brand__name">Brightwell Consulting</span>
    </div>
  </section>

  <section class="card card--back" aria-label="Card back">
    <div class="brand">
      <span class="brand__square"></span>
      <span class="brand__name">Brightwell Consulting</span>
    </div>
    <div class="contact">
      <p class="contact__name">Dorian</p>
      <p class="contact__line">555-010-4477</p>
      <p class="contact__line">dorian@brightwellconsulting.example</p>
      <p class="contact__line">www.brightwellconsulting.example</p>
    </div>
    <p class="tagline">Guidance to Plan Bigger, Act Sooner, Grow Further</p>
  </section>
</body>
</html>
```